New business card design to go with our new logo

just want an eye-catching business card to go with our new logo. We are open to double sided or single sided. Just want it to have the following info on it. Whatever layout you think looks best.

First and Last Name
Title
Phone 801-555-0187
Address 312 W. Larkmoor Avenue Orem UT 84057
Email thecrew@meadowstailandkennel.example

Industry/Entity Type

Business

```html
<!DOCTYPE html>
<html lang="en">
<head>
<meta charset="utf-8">
<title>Meadows Tail &amp; Kennel – Business Card</title>
<link href="https://fonts.googleapis.com/css2?family=Arimo:wght@400;700&display=swap" rel="stylesheet">
<style>
  :root {
    --backdrop: #2b2b2d;
    --brand-blue: #31a6d8;
    --brand-blue-deep: #2d9bcc;
    --brand-orange: #f48a4a;
    --card-white: #ffffff;
    --wash-blue: #eef4fa;
    --wash-orange: #fdf1e8;
    --text-blue: #2f9fd6;
  }
  * { box-sizing: border-box; margin: 0; padding: 0; }
  html, body {
    width: 1189px; height: 1200px; overflow: hidden;
    background: var(--backdrop);
    font-family: "Arimo", Arial, sans-serif;
  }
  .card {
    position: absolute; left: 171px; width: 855px; height: 488px;
    border-radius: 41px; overflow: hidden;
  }
  .card--front { top: 67px; background: var(--brand-blue); }
  .card--back { top: 625px; background: var(--card-white); }

  .decor {
    position: absolute;
  }
  .card--front .decor {
    left: 12px; top: 20px; width: 400px; height: 470px;
    border-radius: 45% 45% 10% 10%;
    background: linear-gradient(180deg, rgba(45,155,204,0.25), rgba(45,155,204,0.55));
  }
  .card--back .decor {
    left: 390px; top: 10px; width: 450px; height: 480px;
    border-radius: 50% 50% 12% 12%;
    background: radial-gradient(circle at 50% 45%, var(--wash-blue) 0 55%, var(--wash-orange) 70%, rgba(255,255,255,0) 78%);
  }

  .front-mark {
    position: absolute; left: 0; right: 0; top: 268px;
    text-align: center; color: var(--card-white); font-weight: 700;
  }
  .front-mark__name { font-size: 58px; letter-spacing: 1px; line-height: 1; }
  .front-mark__sub {
    display: flex; align-items: center; justify-content: center; gap: 8px;
    margin-top: 6px; font-size: 19px; letter-spacing: 1px;
  }
  .front-mark__rule { width: 125px; height: 2px; background: var(--card-white); }

  .back-mark {
    position: absolute; left: 38px; top: 52px; color: var(--brand-orange); font-weight: 700;
  }
  .back-mark__name { font-size: 76px; line-height: 1; letter-spacing: 1px; }
  .back-mark__sub {
    display: flex; align-items: center; gap: 8px; margin-top: 6px;
    font-size: 26px; letter-spacing: 1px;
  }
  .back-mark__rule { width: 190px; height: 2px; background: var(--text-blue); }

  .person { position: absolute; left: 38px; top: 258px; }
  .person__name { color: var(--text-blue); font-weight: 700; font-size: 27px; line-height: 1; }
  .person__title { color: var(--brand-orange); font-size: 20px; line-height: 1.1; }

  .address {
    position: absolute; left: 39px; top: 335px;
    color: var(--text-blue); font-size: 20px; line-height: 26px; font-style: normal;
  }
  .contact { position: absolute; left: 38px; top: 403px; list-style: none; }
  .contact li {
    display: flex; align-items: center; gap: 12px;
    color: var(--text-blue); font-size: 20px; line-height: 24px;
  }
  .contact svg { width: 20px; height: 16px; fill: var(--brand-orange); }
</style>
</head>
<body>
  <section class="card card--front">
    <div class="decor" role="img" aria-label="Faint large illustration of a seated dog"></div>
    <div class="front-mark">
      <div class="front-mark__name">MEADOWS</div>
      <div class="front-mark__sub"><span class="front-mark__rule"></span>TAIL &amp; KENNEL</div>
    </div>
  </section>

  <section class="card card--back">
    <div class="decor" role="img" aria-label="Faint large illustration of a seated dog in a soft ring"></div>
    <div class="back-mark">
      <div class="back-mark__name">MEADOWS</div>
      <div class="back-mark__sub"><span class="back-mark__rule"></span>TAIL &amp; KENNEL</div>
    </div>
    <div class="person">
      <div class="person__name">DANA WHITFIELD</div>
      <div class="person__title">Founder</div>
    </div>
    <address class="address">312 W. Larkmoor Avenue<br>Orem UT 84057</address>
    <ul class="contact">
      <li>
        <svg viewBox="0 0 20 16" aria-hidden="true"><path d="M1 5c4-4 14-4 18 0l-2 2-3-1V4H6v2L3 7z"/><path d="M4 8h12l2 7H2z"/></svg>
        801-555-0187
      </li>
      <li>
        <svg viewBox="0 0 20 16" aria-hidden="true"><path d="M1 1h18v14H1z M2.5 2.5 10 9l7.5-6.5" fill="var(--brand-orange)" stroke="#fff" stroke-width="1.2"/></svg>
        thecrew@meadowstailandkennel.example
      </li>
    </ul>
  </section>
</body>
</html>
```